Financial Services Business Card Design

We are a financial services company Based in London, offering Short term Funding Solutions for companies, raising anywhere between £20,000 and £25million pounds.

The Card must have a professional look as it is going to be handed out to professionals I.E Solicitors, Accountants, Company directors and Business owners.

See Attached our company Logo

Industry/Entity Type

Business

Contact Information for Business Card

Lewis Thorncroft
Suite 41
R K House
Bramblecote Lane
Watford
HP19 4QX

```html
<!DOCTYPE html>
<html lang="en">
<head>
<meta charset="utf-8">
<title>Meridian Funding Centre – Business Card</title>
<link href="https://fonts.googleapis.com/css2?family=Open+Sans:wght@400;600;700&display=swap" rel="stylesheet">
<style>
  :root {
    --brand-blue: #1f6fba;
    --brand-green: #3aaa49;
    --ink: #1c1c1c;
    --card: #ffffff;
    --backdrop: #e6e4e1;
    --rule: #c9c9c9;
  }
  * { margin: 0; padding: 0; box-sizing: border-box; }
  html, body {
    width: 1200px; height: 1000px; overflow: hidden;
    background: var(--backdrop);
    font-family: "Open Sans", Arial, sans-serif;
  }
  .canvas { position: relative; width: 1200px; height: 1000px; }
  .card {
    position: absolute; left: 265px; width: 666px; height: 398px;
    background: var(--card); overflow: hidden;
    box-shadow: 0 3px 10px rgba(0,0,0,0.18);
  }
  .card--front { top: 73px; }
  .card--back { top: 532px; }
  .card__swoosh { position: absolute; left: 0; bottom: 0; width: 666px; }
  .card--front .card__swoosh { height: 50px; }
  .card--back .card__swoosh { height: 80px; }

  .brand { position: absolute; left: 0; width: 100%; text-align: center; }
  .brand__dot {
    display: block; margin: 0 auto; border-radius: 50%;
    background: var(--brand-green);
  }
  .brand__name {
    display: block; color: var(--brand-blue); font-weight: 700;
    letter-spacing: 0.5px; line-height: 1.1;
  }
  .card--front .brand { top: 40px; }
  .card--front .brand__dot { width: 70px; height: 70px; margin-bottom: 30px; }
  .card--front .brand__name { font-size: 30px; }
  .card--back .brand { top: 88px; }
  .card--back .brand__dot { width: 90px; height: 90px; margin-bottom: 38px; }
  .card--back .brand__name { font-size: 36px; }

  .person {
    position: absolute; right: calc(666px - 313px); top: 255px; text-align: right;
  }
  .person__name { color: var(--brand-blue); font-size: 22px; font-weight: 600; line-height: 1.25; }
  .person__title { color: var(--ink); font-size: 16px; line-height: 1.4; }
  .divider {
    position: absolute; left: 333px; top: 235px; width: 1px; height: 102px;
    background: linear-gradient(to bottom, transparent, var(--rule), transparent);
  }
  .contact { position: absolute; left: 353px; top: 228px; color: var(--ink); font-size: 16px; }
  .contact__address { line-height: 22px; margin-bottom: 4px; }
  .contact__line { display: flex; align-items: center; height: 22px; }
  .contact__icon { width: 16px; height: 14px; margin-right: 9px; fill: var(--brand-blue); }
  .card__url {
    position: absolute; left: 0; width: 100%; bottom: 5px; text-align: center;
    color: #ffffff; font-size: 16px; letter-spacing: 0.5px;
  }
</style>
</head>
<body>
<div class="canvas">

  <section class="card card--front">
    <div class="brand">
      <span class="brand__dot"></span>
      <span class="brand__name">MERIDIAN FUNDING CENTRE</span>
    </div>

    <div class="person">
      <p class="person__name">Lewis Thorncroft</p>
      <p class="person__title">Managing Director</p>
    </div>
    <div class="divider"></div>
    <div class="contact">
      <p class="contact__address">Suite 41 R K House<br>Bramblecote Lane Watford, HP19 4QX</p>
      <p class="contact__line">
        <svg class="contact__icon" viewBox="0 0 16 14"><path d="M1 4c2-3 12-3 14 0l-1 2-3-1V3H5v2L2 6zM4 7h8l2 6H2z"/></svg>
        + 000 000 0000
      </p>
      <p class="contact__line">
        <svg class="contact__icon" viewBox="0 0 16 14"><rect x="4" y="0" width="8" height="4"/><rect x="1" y="5" width="14" height="6" rx="1"/><rect x="4" y="9" width="8" height="5"/></svg>
        + 000 000 0000
      </p>
      <p class="contact__line">
        <svg class="contact__icon" viewBox="0 0 16 14"><path d="M1 2h14v1L8 8 1 3zM1 5l7 5 7-5v7H1z"/></svg>
        info@meridianfunding.com
      </p>
    </div>

    <svg class="card__swoosh" viewBox="0 0 666 50" preserveAspectRatio="none">
      <path d="M60 22 Q333 -8 620 22 Q333 4 60 22Z" fill="var(--brand-green)"/>
      <path d="M0 37 Q333 10 666 37 L666 50 L0 50Z" fill="var(--brand-blue)"/>
    </svg>
    <p class="card__url">www.meridianfunding.com</p>
  </section>

  <section class="card card--back">
    <div class="brand">
      <span class="brand__dot"></span>
      <span class="brand__name">MERIDIAN FUNDING CENTRE</span>
    </div>
    <svg class="card__swoosh" viewBox="0 0 666 80" preserveAspectRatio="none">
      <path d="M0 20 Q300 40 666 34 Q300 50 0 36Z" fill="var(--brand-green)"/>
      <path d="M0 42 Q300 56 666 38 L666 80 L0 80Z" fill="var(--brand-blue)"/>
    </svg>
  </section>

</div>
</body>
</html>
```